Webshop for baby shoes need new design

We are an innovative company selling a one of a kind product on a market with tough competition. We are looking to step up our business and need a new design for our shop.

We are looking for recognition as well as originality. The customer must immediately be able to identify navigation, shopping cart, buy buttons etc. We want warm welcoming colors, but not too strong as to not draw attention away from the products. Retro might be interesting, if "done right".

Suggested color palette: http://huepalettemaker.example/#7k29WbQx3p8r5

We have a logo (attached), but if you have a better idea we might go for that instead. Also, a couple of product images are attached for you to use in the design.

What we do NOT want is a shop that looks like a free template (vendaForge etc). Also, while we are selling baby shoes, we don't want to use the very worn our baby pink/blue scheme, so stay clear of this, thanks.
Updates

We suggest that you use this palette, or similar: http://huepalettemaker.example/#7k29WbQx3p8r5

Project Deadline Extended
Reason: We feel that we are getting closer to finding a design that we like, but there is still a bit to go. Also we want to give the chance to any late starters to show their idea. The competition is still open.

Target Market(s)

babies and their parents

Industry/Entity Type

Shopping

Requirements
Must have
• The usual webshop elements
- shopping cart
- product listing
- product page
- buy buttons
Nice to have
• - large footer area for links, info and function (see trindel.example for an example)
- some kind of product navigation/filter (left, top or right)
- place for promotion banners

```html
<!DOCTYPE html>
<html lang="en">
<head>
<meta charset="utf-8">
<title>Baby Shoes Shop – New Products</title>
<link rel="stylesheet" href="https://fonts.googleapis.com/css2?family=Questrial&display=swap">
<style>
  :root{
    --outer-bg:#e9e6de;
    --page-bg:#f5f3ed;
    --card-bg:#faf8f3;
    --card-border:#eadcc7;
    --heading:#4e3018;
    --subtext:#8c6a46;
    --price:#c8102e;
    --dash:#ddd3c4;
    --icon:#a88a68;
    --dot:#dccfbf;
    --dot-active:#a87b4f;
    --white:#ffffff;
  }
  *{box-sizing:border-box;margin:0;padding:0}
  html,body{width:1200px;height:900px;overflow:hidden}
  body{background:var(--outer-bg);font-family:"Questrial","Century Gothic",sans-serif;position:relative}
  .page{position:absolute;left:41px;top:0;width:1118px;height:900px;background:var(--page-bg)}
  .slider-box{position:absolute;left:195px;top:-10px;width:811px;height:55px;background:var(--card-bg);border:2px solid var(--card-border);border-top:none;border-radius:0 0 6px 6px}
  .slider-dots{position:absolute;left:566px;top:14px;display:flex;gap:7px}
  .slider-dots span{width:12px;height:12px;border-radius:50%;background:var(--dot)}
  .slider-dots .is-active{background:var(--dot-active)}
  .product-section{position:absolute;left:195px;width:811px;height:400px}
  .section-title{position:absolute;left:1px;top:0;font-size:19px;font-weight:400;letter-spacing:.3px;color:var(--heading);line-height:22px}
  .section-rule{position:absolute;left:0;top:27px;width:811px;border-top:1px dashed var(--dash)}
  .product-card{position:absolute;top:50px;width:248px;height:322px;background:var(--card-bg);border:2px solid var(--card-border);border-radius:5px}
  .product-name{position:absolute;left:20px;top:9px;font-size:18px;font-weight:400;color:var(--heading);line-height:22px}
  .product-desc{position:absolute;left:20px;top:29px;font-size:14px;color:var(--subtext);line-height:16px}
  .product-image{position:absolute;left:17px;top:52px;width:211px;height:210px;background:var(--white);border:1px solid var(--card-border)}
  .product-image .photo{position:absolute;left:22px;top:50px;width:166px;height:115px;border-radius:40% 50% 12% 12%}
  .photo-navy{background:radial-gradient(ellipse at 55% 55%,#26336b 0%,#4d6aa8 55%,#ffffff 100%)}
  .photo-orange{background:radial-gradient(ellipse at 55% 55%,#1f2c63 0%,#5a5a7a 50%,#e08850 75%,#ffffff 100%)}
  .photo-teal{background:radial-gradient(ellipse at 55% 55%,#1d5f73 0%,#3d7e92 55%,#ffffff 100%)}
  .price{position:absolute;left:24px;top:276px;font-size:20px;color:var(--price);line-height:24px}
  .action-btn{position:absolute;top:272px;width:40px;height:36px;background:var(--white);border:1px solid var(--card-border);display:flex;align-items:center;justify-content:center}
  .btn-wish{left:143px}
  .btn-cart{left:188px}
  .view-more{position:absolute;right:1px;top:380px;font-size:11px;color:var(--subtext);text-decoration:underline}
</style>
</head>
<body>
<div class="page"></div>

<div class="slider-box">
  <div class="slider-dots"><span></span><span class="is-active"></span><span></span><span></span></div>
</div>

<section class="product-section" style="top:74px">
  <h2 class="section-title">NEW PRODUCTS</h2>
  <div class="section-rule"></div>

  <article class="product-card" style="left:0">
    <h3 class="product-name">PRODUCT 1 NAME</h3>
    <p class="product-desc">MINI DESCRIPTION</p>
    <div class="product-image"><div class="photo photo-navy" role="img" aria-label="Navy and light blue lace-up baby shoe"></div></div>
    <span class="price">49,00€</span>
    <a class="action-btn btn-wish" aria-label="Add to wishlist"><svg width="20" height="20" viewBox="0 0 24 24"><path d="M12 2.5l2.9 6.2 6.6.7-5 4.5 1.4 6.6L12 17.2l-5.9 3.3 1.4-6.6-5-4.5 6.6-.7z" fill="none" stroke="var(--icon)" stroke-width="1.6" stroke-linejoin="round"/></svg></a>
    <a class="action-btn btn-cart" aria-label="Add to cart"><svg width="26" height="22" viewBox="0 0 26 22"><path d="M1 2h4l3 12h13l3-9H7" fill="none" stroke="var(--icon)" stroke-width="1.6" stroke-linejoin="round"/><path d="M9 6v6M13 6v6M17 6v6M21 6v5" stroke="var(--icon)" stroke-width="1"/><circle cx="10" cy="18" r="1.8" fill="none" stroke="var(--icon)" stroke-width="1.4"/><circle cx="19" cy="18" r="1.8" fill="none" stroke="var(--icon)" stroke-width="1.4"/></svg></a>
  </article>

  <article class="product-card" style="left:282px">
    <h3 class="product-name">PRODUCT 2 NAME</h3>
    <p class="product-desc">MINI DESCRIPTION</p>
    <div class="product-image"><div class="photo photo-orange" role="img" aria-label="Navy baby shoe with orange accents and side zip"></div></div>
    <span class="price">49,00€</span>
    <a class="action-btn btn-wish" aria-label="Add to wishlist"><svg width="20" height="20" viewBox="0 0 24 24"><path d="M12 2.5l2.9 6.2 6.6.7-5 4.5 1.4 6.6L12 17.2l-5.9 3.3 1.4-6.6-5-4.5 6.6-.7z" fill="none" stroke="var(--icon)" stroke-width="1.6" stroke-linejoin="round"/></svg></a>
    <a class="action-btn btn-cart" aria-label="Add to cart"><svg width="26" height="22" viewBox="0 0 26 22"><path d="M1 2h4l3 12h13l3-9H7" fill="none" stroke="var(--icon)" stroke-width="1.6" stroke-linejoin="round"/><path d="M9 6v6M13 6v6M17 6v6M21 6v5" stroke="var(--icon)" stroke-width="1"/><circle cx="10" cy="18" r="1.8" fill="none" stroke="var(--icon)" stroke-width="1.4"/><circle cx="19" cy="18" r="1.8" fill="none" stroke="var(--icon)" stroke-width="1.4"/></svg></a>
  </article>

  <article class="product-card" style="left:562px">
    <h3 class="product-name">PRODUCT 3 NAME</h3>
    <p class="product-desc">MINI DESCRIPTION</p>
    <div class="product-image"><div class="photo photo-teal" role="img" aria-label="Teal baby shoe with strap closure"></div></div>
    <span class="price">49,00€</span>
    <a class="action-btn btn-wish" aria-label="Add to wishlist"><svg width="20" height="20" viewBox="0 0 24 24"><path d="M12 2.5l2.9 6.2 6.6.7-5 4.5 1.4 6.6L12 17.2l-5.9 3.3 1.4-6.6-5-4.5 6.6-.7z" fill="none" stroke="var(--icon)" stroke-width="1.6" stroke-linejoin="round"/></svg></a>
    <a class="action-btn btn-cart" aria-label="Add to cart"><svg width="26" height="22" viewBox="0 0 26 22"><path d="M1 2h4l3 12h13l3-9H7" fill="none" stroke="var(--icon)" stroke-width="1.6" stroke-linejoin="round"/><path d="M9 6v6M13 6v6M17 6v6M21 6v5" stroke="var(--icon)" stroke-width="1"/><circle cx="10" cy="18" r="1.8" fill="none" stroke="var(--icon)" stroke-width="1.4"/><circle cx="19" cy="18" r="1.8" fill="none" stroke="var(--icon)" stroke-width="1.4"/></svg></a>
  </article>

  <a class="view-more">view more</a>
</section>

<section class="product-section" style="top:485px">
  <h2 class="section-title">NEW PRODUCTS</h2>
  <div class="section-rule"></div>

  <article class="product-card" style="left:0">
    <h3 class="product-name">PRODUCT 1 NAME</h3>
    <p class="product-desc">MINI DESCRIPTION</p>
    <div class="product-image"><div class="photo photo-navy" role="img" aria-label="Navy and light blue lace-up baby shoe"></div></div>
    <span class="price">49,00€</span>
    <a class="action-btn btn-wish" aria-label="Add to wishlist"><svg width="20" height="20" viewBox="0 0 24 24"><path d="M12 2.5l2.9 6.2 6.6.7-5 4.5 1.4 6.6L12 17.2l-5.9 3.3 1.4-6.6-5-4.5 6.6-.7z" fill="none" stroke="var(--icon)" stroke-width="1.6" stroke-linejoin="round"/></svg></a>
    <a class="action-btn btn-cart" aria-label="Add to cart"><svg width="26" height="22" viewBox="0 0 26 22"><path d="M1 2h4l3 12h13l3-9H7" fill="none" stroke="var(--icon)" stroke-width="1.6" stroke-linejoin="round"/><path d="M9 6v6M13 6v6M17 6v6M21 6v5" stroke="var(--icon)" stroke-width="1"/><circle cx="10" cy="18" r="1.8" fill="none" stroke="var(--icon)" stroke-width="1.4"/><circle cx="19" cy="18" r="1.8" fill="none" stroke="var(--icon)" stroke-width="1.4"/></svg></a>
  </article>

  <article class="product-card" style="left:282px">
    <h3 class="product-name">PRODUCT 2 NAME</h3>
    <p class="product-desc">MINI DESCRIPTION</p>
    <div class="product-image"><div class="photo photo-orange" role="img" aria-label="Navy baby shoe with orange accents and side zip"></div></div>
    <span class="price">49,00€</span>
    <a class="action-btn btn-wish" aria-label="Add to wishlist"><svg width="20" height="20" viewBox="0 0 24 24"><path d="M12 2.5l2.9 6.2 6.6.7-5 4.5 1.4 6.6L12 17.2l-5.9 3.3 1.4-6.6-5-4.5 6.6-.7z" fill="none" stroke="var(--icon)" stroke-width="1.6" stroke-linejoin="round"/></svg></a>
    <a class="action-btn btn-cart" aria-label="Add to cart"><svg width="26" height="22" viewBox="0 0 26 22"><path d="M1 2h4l3 12h13l3-9H7" fill="none" stroke="var(--icon)" stroke-width="1.6" stroke-linejoin="round"/><path d="M9 6v6M13 6v6M17 6v6M21 6v5" stroke="var(--icon)" stroke-width="1"/><circle cx="10" cy="18" r="1.8" fill="none" stroke="var(--icon)" stroke-width="1.4"/><circle cx="19" cy="18" r="1.8" fill="none" stroke="var(--icon)" stroke-width="1.4"/></svg></a>
  </article>

  <article class="product-card" style="left:562px">
    <h3 class="product-name">PRODUCT 3 NAME</h3>
    <p class="product-desc">MINI DESCRIPTION</p>
    <div class="product-image"><div class="photo photo-teal" role="img" aria-label="Teal baby shoe with strap closure"></div></div>
    <span class="price">49,00€</span>
    <a class="action-btn btn-wish" aria-label="Add to wishlist"><svg width="20" height="20" viewBox="0 0 24 24"><path d="M12 2.5l2.9 6.2 6.6.7-5 4.5 1.4 6.6L12 17.2l-5.9 3.3 1.4-6.6-5-4.5 6.6-.7z" fill="none" stroke="var(--icon)" stroke-width="1.6" stroke-linejoin="round"/></svg></a>
    <a class="action-btn btn-cart" aria-label="Add to cart"><svg width="26" height="22" viewBox="0 0 26 22"><path d="M1 2h4l3 12h13l3-9H7" fill="none" stroke="var(--icon)" stroke-width="1.6" stroke-linejoin="round"/><path d="M9 6v6M13 6v6M17 6v6M21 6v5" stroke="var(--icon)" stroke-width="1"/><circle cx="10" cy="18" r="1.8" fill="none" stroke="var(--icon)" stroke-width="1.4"/><circle cx="19" cy="18" r="1.8" fill="none" stroke="var(--icon)" stroke-width="1.4"/></svg></a>
  </article>

  <a class="view-more">view more</a>
</section>
</body>
</html>
```